Design a cool print brochure for an NGO / Give your work a global impact!!

Hi,
I provide a full design brief (below, please scroll) and a mood board (attached) to help you visualize inside my head.. ;-)
I am also available to help and have worked many years in advertising; we will understand each other.
Objective:
To design an A4 folded in two presentation brochure for a non-profit consulting agency called Mer-ova.
Mer-ova works in sustainability and international development = working with NGO’s, governments and private sector on global issues such as global warming, education for all etc.
Strategy:
This document is a first step in developing a communication strategy. It will be distributed during a major international event called the Brenvik Outreach Forum.
Objective:
The double objective of the brochure is:
a) to inform the recipient of what Mer-ova is, in the shortest time possible.
b) to showcase relevant projects to demonstrate Mer-ova experience and expertise.
Target:
Main target:
Existing Mer-ova contacts, such as members of development organizations, NGOs, private sector foundations (CSR), regional networks and other development actors.
NB: the main target already has a certain awareness of Mer-ova: we will try to minimize text to maximize visual impact and readability.
Secondary target:
Mer-ova will also distribute the brochure to new prospects of interest during the Brenvik Forum.
Timing:
We will need to finalize the design and have the files by June 1st to allow time for print before the event.
Content:
The document should be concise, highly readable (no clutter) and include:
1. text (that we will provide)
and
2. visual elements such as images, shapes and info-graphics (that is you).
NB: Mer-ova does not have its own image bank; photos will be provided by you.
Format:
A4 folded in half - 4pp A5 - PORTRAIT FORMAT) with an impactful visual in the front, logo, title and headline (please see examples in the mood board attached).
Design elements:
Mer-ova does not have yet a visual identity (please see: http://mer-ova.org) so there is room for creativity and no graphic chart to follow.
The sector of consulting in international development is rather conservative but our intention is to be disruptive and create a “Wow” effect. We count on you for that!
Therefore, the design should be “structured”, “organized”, “uncluttered” but also “modern”, “impactful”, “highly visual” (think infographic or mind map to describe our services and projects).
Please, take the time to see the attached presentation: I give you guidelines and examples of what we want and what we like.
We are looking forward to seeing your work and I am available for comments, questions and support.
Thank you.
RM
Target Market(s)
The full brief is in the project description: please, scroll through it.
The target market is : our existing clients base, working in sustainable development (read: NGO and Concord Assembly people)
Industry/Entity Type
Ngo
Requirements
Must have
- - Design and color elements: please, no black and white. Our company website is in black and white and without graphics; we want the brochure to break away from that and start creating our brand identity; so please, show us colors and desing elements (shapes, backgrounds, etc).
- You have a chance to showcase your talent in terms of visual identity: what lines, forms, layout and colors can you come up with and apply throughout the brochure and serve as the visual identity of Mer-ova?
- The structure of the document should be:
- - Front cover: design elements + impacful photo (see mood board example attached) +our logo + this headline: "Collective action for sustainable development and impact"
- - Inside front: a graphic representation of "Our Services": such as core activity in the center circle and satellite circles for the services we offer.
- - Inside back:
- 1. Icons and text boxes for "Our projects"
- 2. A world map of the countries where we have worked. Full list of countries is here:
- http://mer-ova.org/experience-1
- - Back cover: our contact + logos of partners.
- Our partners are listed here:
- Please use their original logos (ie, in color).
- The design we will select will serve as a basis for a graphic chart...so more work to come...word to the wise ;)
- Please check out our website mer-ova.org to see what we do etc.
Nice to have
- Icons to reflect our services: what icons can you come up with to describe "training services", "building networks" or "program management"?
- I give examples in the mood board.
Should not have
- We are open to creativity and want to generate a "Wow" effect.
- Just note that the sector is rather conservative so flashy colors and cartoon like characters should be avoided. Think "earth, global change, Concord Assembly, climate" without going too green (it's overdone). ;-)
- Make us stand out in the NGO world
- Now you.

```html
<!DOCTYPE html>
<html lang="en">
<head>
<meta charset="utf-8">
<title>Mer-ova brochure — outer spread</title>
<link href="https://fonts.googleapis.com/css2?family=Montserrat:wght@300;400;500;600;700;800&family=Raleway:wght@500&display=swap" rel="stylesheet">
<style>
  :root{
    --bg:#c9c9c9;
    --paper:#fbfbfb;
    --teal:#159e82;
    --teal-dark:#0f7f69;
    --orange:#ee7a2c;
    --ink:#141414;
    --photo-light:#e4e8ec;
    --photo-mid:#9aa3ad;
    --photo-dark:#4b525b;
    --white:#ffffff;
  }
  *{box-sizing:border-box;margin:0;padding:0}
  html,body{width:1200px;height:960px;overflow:hidden;background:var(--bg)}
  .spread{
    position:absolute;left:50px;top:91px;width:1100px;height:778px;
    display:flex;background:var(--paper);
    box-shadow:0 6px 24px rgba(0,0,0,.18);
  }
  .panel{position:relative;width:550px;height:778px;overflow:hidden}

  /* back cover */
  .back{background:var(--paper)}
  .back .corner{position:absolute;left:0;top:0}
  .back .about{
    position:absolute;left:110px;top:120px;width:340px;
    font-family:"Raleway",sans-serif;font-weight:500;font-variant:small-caps;
    font-size:22px;line-height:1.32;letter-spacing:.04em;
    color:var(--orange);text-align:center;
  }
  .contact{
    position:absolute;left:150px;top:430px;list-style:none;
    font-family:"Montserrat",sans-serif;font-weight:700;font-size:22px;
    color:var(--teal);letter-spacing:.01em;
  }
  .contact li{display:flex;align-items:center;gap:10px;margin-bottom:18px}
  .contact svg{flex:none}
  .back .brand{position:absolute;left:260px;top:610px;color:var(--ink)}

  /* name lockup: plain text in the piece's own font */
  .brand .name{
    display:flex;align-items:center;gap:12px;
    font-family:"Montserrat",sans-serif;font-weight:600;font-size:44px;line-height:1;
  }
  .brand .mark{width:14px;height:14px;background:var(--teal);flex:none}
  .brand .tagline{
    margin-top:12px;max-width:230px;
    font-family:"Montserrat",sans-serif;font-weight:500;font-size:13px;line-height:1.35;
  }

  /* front cover */
  .front .photo{position:absolute;inset:0;
    background:
      radial-gradient(ellipse at 70% 45%, rgba(255,255,255,.55), transparent 55%),
      linear-gradient(160deg,var(--photo-light) 0%,var(--photo-mid) 48%,var(--photo-dark) 100%);
  }
  .front .facets{position:absolute;inset:0}
  .front .brand{position:absolute;left:150px;top:150px;color:var(--white)}
  .headline{
    position:absolute;left:0;top:470px;width:550px;height:190px;
    background:rgba(255,255,255,.85);
    padding:18px 40px 0 0;text-align:right;
    font-family:"Montserrat",sans-serif;text-transform:uppercase;line-height:1.05;
  }
  .headline .line{display:block}
  .headline .l1{color:var(--orange);font-weight:800;font-size:31px;border-top:3px solid var(--orange);display:inline-block;padding-top:4px}
  .headline .l2{color:var(--ink);font-weight:300;font-size:31px;letter-spacing:.03em}
  .headline .l3{color:var(--teal);font-weight:700;font-size:40px;letter-spacing:.02em}
  .headline .l4{color:var(--ink);font-weight:800;font-size:27px;display:inline-block;border-bottom:3px solid var(--orange);padding-bottom:4px}
</style>
</head>
<body>
<main class="spread">
  <section class="panel back">
    <svg class="corner" width="30" height="22" viewBox="0 0 30 22"><polygon points="0,0 30,0 0,22" fill="var(--orange)"/></svg>
    <p class="about">We are based in different cities in Europe. You can contact any of us directly in About Us. Alternatively, for general inquiries, you can use the number and/or email below.</p>
    <ul class="contact">
      <li>
        <svg width="22" height="22" viewBox="0 0 24 24"><path d="M6.6 10.8a15 15 0 0 0 6.6 6.6l2.2-2.2c.3-.3.7-.4 1-.2 1.1.4 2.300.6 3.6.6.6 0 1 .4 1 1V20c0 .6-.4 1-1 1A17 17 0 0 1 3 4c0-.6.4-1 1-1h3.5c.6 0 1 .4 1 1 0 1.3.2 2.5.6 3.6.1.3 0 .7-.2 1z" fill="var(--ink)"/></svg>
        +34 611 482 907
      </li>
      <li>
        <svg width="24" height="24" viewBox="0 0 24 24"><circle cx="12" cy="12" r="12" fill="var(--ink)"/><rect x="6" y="8" width="12" height="8" fill="none" stroke="var(--white)" stroke-width="1.2"/><polyline points="6,8 12,13 18,8" fill="none" stroke="var(--white)" stroke-width="1.2"/></svg>
        INFO@MER-OVA.ORG
      </li>
    </ul>
    <div class="brand">
      <div class="name"><span class="mark"></span>Mer-ova</div>
      <p class="tagline">Analysis and advisory services for effective collaborative action</p>
    </div>
  </section>

  <section class="panel front">
    <div class="photo" role="img" aria-label="Photo: a hand using a tablet on an office desk, softly blurred"></div>
    <svg class="facets" width="550" height="778" viewBox="0 0 550 778">
      <polygon points="0,0 550,0 550,95" fill="var(--teal)"/>
      <polygon points="300,0 550,0 550,60" fill="var(--teal-dark)" opacity=".5"/>
      <polygon points="550,662 550,778 300,778" fill="var(--teal)"/>
      <polygon points="550,710 550,778 420,778" fill="var(--teal-dark)" opacity=".5"/>
    </svg>
    <div class="brand">
      <div class="name"><span class="mark"></span>Mer-ova</div>
      <p class="tagline">Analysis and advisory services for effective collaborative action</p>
    </div>
    <h1 class="headline">
      <span class="line"><span class="l1">Collective action</span></span>
      <span class="line l2">for sustainable</span>
      <span class="line l3">development</span>
      <span class="line"><span class="l4">and impact</span></span>
    </h1>
  </section>
</main>
</body>
</html>
```